Tidewater Guest Consulting

I am an independent operator engaged on short/medium term consultancy briefs within the Hotel/Resort sector in the Pacific Area and have a representation in Fiji.

A broad based services is offered and includes:

Development Advisory
Property Management
Sales & Marketing
Holiday Ownership/Timeshare
Resorts/Apartments/Motels/Flashpackers/B&B
Financial & Legal Referrals

Industry/Entity Type

Hotel

Contact Information for Business Card

Business name - TIDEWATER GUEST CONSULTING
My name - Marcus Holt
Address: PO Box 318 Coral Heath 4871 Qld
Phone: Australia: +61 7 55019284 Mobile: 0414093857 (Viber)
Fiji: +679 8230519
Email: marcuswholt@tealnest-mail.com

```html
<!DOCTYPE html>
<html lang="en">
<head>
<meta charset="utf-8">
<title>Tidewater Guest Consulting – Business Card</title>
<link rel="stylesheet" href="https://fonts.googleapis.com/css2?family=Cormorant+Garamond:ital,wght@0,500;0,600;1,500&display=swap">
<style>
  :root {
    --backdrop: #ece6dc;
    --card-red: #8c1821;
    --card-red-deep: #6a0f17;
    --card-edge: #5a0b12;
    --silver: #ecebe9;
    --silver-soft: #c9c6c2;
    --text-silver: #efe9e6;
  }
  * { box-sizing: border-box; margin: 0; padding: 0; }
  html, body {
    width: 1200px;
    height: 1000px;
    overflow: hidden;
    background: var(--backdrop);
    font-family: "Cormorant Garamond", Georgia, serif;
  }
  .canvas {
    position: relative;
    width: 1200px;
    height: 1000px;
  }
  .card {
    position: absolute;
    left: 240px;
    width: 720px;
    height: 410px;
    background: radial-gradient(ellipse at 40% 30%, var(--card-red) 0%, var(--card-red-deep) 100%);
    border-radius: 4px;
    box-shadow: 0 4px 0 var(--card-edge), 0 14px 28px rgba(60, 20, 20, 0.25);
    color: var(--text-silver);
    overflow: hidden;
  }
  .card--front { top: 60px; }
  .card--back { top: 530px; }

  .brand {
    position: absolute;
    display: flex;
    align-items: center;
    gap: 16px;
  }
  .brand__mark {
    width: 62px;
    height: 62px;
    border-radius: 50%;
    background: var(--silver);
    flex: none;
  }
  .brand__name {
    font-weight: 600;
    color: var(--silver);
    letter-spacing: 0.5px;
  }
  .ornament {
    position: absolute;
    border-radius: 30px;
    background: radial-gradient(ellipse at center, rgba(236, 235, 233, 0.28), rgba(236, 235, 233, 0));
  }

  /* front face */
  .card--front .ornament { left: 150px; top: 46px; width: 420px; height: 150px; }
  .card--front .brand { left: 0; right: 0; top: 90px; justify-content: center; }
  .card--front .brand__name { font-size: 38px; }
  .services {
    position: absolute;
    left: 60px;
    right: 60px;
    top: 230px;
    text-align: center;
    font-style: italic;
    font-weight: 500;
    font-size: 19px;
    line-height: 1.65;
    color: var(--text-silver);
  }

  /* back face */
  .card--back .ornament { left: 330px; top: 30px; width: 360px; height: 140px; }
  .card--back .brand { right: 44px; top: 70px; }
  .card--back .brand__name { font-size: 30px; }
  .holder {
    position: absolute;
    left: 48px;
    top: 190px;
    font-weight: 600;
    font-size: 34px;
    letter-spacing: 2px;
    color: var(--silver);
  }
  .contacts {
    position: absolute;
    left: 48px;
    right: 40px;
    bottom: 40px;
    font-style: italic;
    font-weight: 500;
    font-size: 17px;
    line-height: 1.7;
    color: var(--text-silver);
  }
  .contacts__row { display: flex; gap: 22px; }
</style>
</head>
<body>
<main class="canvas">
  <section class="card card--front">
    <div class="ornament" role="img" aria-label="Silver floral flourish with stars framing the emblem"></div>
    <div class="brand">
      <span class="brand__mark"></span>
      <span class="brand__name">Tidewater Guest Consulting</span>
    </div>
    <p class="services">
      Development Advisory | Property Management | Sales &amp; Marketing<br>
      Holiday Ownership/Timeshare | Resorts|Apartments|Motels|Flashpackers|B&amp;B |<br>
      Financial &amp; Legal Referrals
    </p>
  </section>

  <section class="card card--back">
    <div class="ornament" role="img" aria-label="Silver floral flourish with stars framing the emblem"></div>
    <div class="brand">
      <span class="brand__mark"></span>
      <span class="brand__name">Tidewater Guest Consulting</span>
    </div>
    <h1 class="holder">MARCUS HOLT</h1>
    <div class="contacts">
      <div class="contacts__row">
        <span>Mobile: 0414093857</span>
        <span>Phone: +61 7 55019284 (Australia)</span>
        <span>Viber: +679 8230519 (Fiji)</span>
      </div>
      <div class="contacts__row">
        <span>Email: marcuswholt@tealnest-mail.com</span>
        <span>PO Box 318 Coral Heath 4871 Qld</span>
      </div>
    </div>
  </section>
</main>
</body>
</html>
```